MODERN + COOL Business Card Needed!

SUMMARY
This is for a 40+ year old family business that is transitioning to the 2nd generation and is in real need of a more modern facelift. Ive attached a company logo (I made quickly as an idea with my limited PSD skills) to start off with that you are welcome to change and draw ideas from. Ive also attached some screen shots of cards I like to give you an idea of my preferences.

WHAT WE DO
The company name is Tall Pine HK Ltd. But I prefer to just call it Tall Pine or Tall Pine with Hong Kong as kind of a sub heading on the business card. We own a factory as well as help our customers find factories to make their product. Product I mean, toys 99.9% of the time. Simple old school toys like board games, puzzles, wooden toys, baby/infant toys.

You can say we are a "sourcing" or "trading" or "consulting" company with a factory to help you do it. But since we deal with toys, i like to keep it modern and cool and fun, not serious like managing hedge funds.

WHAT WE ARE LOOKING FOR
A cool, unique looking business card that stands out. In terms of design, something modern and professional. I like darker colored cards and I like colors such as blue/green/dark gray, but am open to other colored themes. I Like bright lime green with gray, always though thats a nice combo. I prefer cards that are all colored and not so much white showing (I think). Ive attached a few screenshots of cards so take a look to get a feel of what I like.

We do alot of wooden stacking games in variety of colors too like Tovra, Lumo, Towerplix (google these to check them out). So designs that sort of resemble stacking or building would be cool but totally not necessary.

In terms of the physical aspects of the card, Im looking for a card a bit different than the standard rectangular shape. Double sided. Little things like having corner(s) be round or different angle instead of square edge I always thought was nice. Its got to be mostly a normal card size, no folding or smaller cards that fit weird in your wallet. No vertical designs. Am open to VERY different/creative shapes (as long as it still fits in a wallet good like a normal buisness card.
Updates

Hi everyone!

Just wanted to write a message to everyone to let them know all submissions are being reviewed or have been reviewed.  If I have not responded with feedback, rest assure your submission was definitely looked at in detail but I either have just been too busy to respond (alot of submissions!), or its on my to be considered list.

I respect and really enjoy receiving everyones creativity and work so I dont want it to go unrecognized - thus this message!  Feel free to submit more ideas if you like until this project ends.  Sometimes some designs just dont click but sometimes they can so you never know!

Thanks again for everyones participation and great work!

~Dev Orr

Target Market(s)

The cards are mainly handed to toy company sourcers and buyers. People I talk to ... say Pelvane for example... might want to make their next edition of Farthingale game with a reputable factory at a good cost so they can sell it to stores at a profit.

So these are the types of people I often try to talk and introduce myself and my company to.

Industry/Entity Type

Building

Colors
acd036
0392cd
00a88e
474747
606060

Requirements
Must have
• Just double sided, not plain rectangle corners, and just cool to look at and catches your eye!

Oh and the obvious business card stuff like place for name, address, number, email, etc.
Nice to have
• Think more modern and fun, not serious and old fashion (thats what we used to be!). Can use the logo I attached and you can definitely alter and change the logo or make a whole new one!

Oh and can definitely use a creative slogan if you like to think of one based on what I described in what we do.
Should not have
• Dont use fonts or text placement that might make "Tall Pine" look like "Tal Lpine"... We arent selling news papers!!

Please nothing related to education since we have the word Pine in the title, thats not our business at all.

Logo and design should not be too heavy on things related to toys, as though thats what we primarily focus on now, what we do may change over time.

```html
<!DOCTYPE html>
<html lang="en">
<head>
<meta charset="utf-8">
<title>Tall Pine Hong Kong – Business Card</title>
<link rel="stylesheet" href="https://fonts.googleapis.com/css2?family=Arimo:wght@400;700&family=Lilita+One&display=swap">
<style>
  :root {
    --lime: #acd036;
    --lime-deep: #8fae2a;
    --blue: #0392cd;
    --teal: #00a88e;
    --gray-dark: #474747;
    --gray-mid: #606060;
    --ink: #111111;
    --backdrop: #2b2b2b;
    --pattern-base: #5d6b78;
    --pattern-tone: #2f8fc0;
  }
  * { margin: 0; padding: 0; box-sizing: border-box; }
  html, body {
    width: 1200px;
    height: 900px;
    overflow: hidden;
    background: var(--backdrop);
  }
  .canvas {
    position: relative;
    width: 1200px;
    height: 900px;
  }
  .card {
    position: absolute;
    left: 220px;
    width: 760px;
    height: 420px;
    border-radius: 28px;
    overflow: hidden;
    box-shadow: 0 12px 30px rgba(0,0,0,0.5);
  }
  .card--front { top: 26px; }
  .card--back { top: 464px; }
  .card svg.card-art {
    position: absolute;
    inset: 0;
    width: 100%;
    height: 100%;
  }
  .brand {
    position: absolute;
    display: flex;
    align-items: center;
    gap: 14px;
    font-family: "Lilita One", sans-serif;
    text-transform: uppercase;
    line-height: 0.95;
    letter-spacing: 1px;
    white-space: nowrap;
  }
  .brand__dot {
    width: 58px;
    height: 58px;
    border-radius: 50%;
    flex: none;
  }
  .brand__name { font-size: 30px; }
  .brand--front { right: 48px; top: 150px; }
  .brand--front .brand__dot { background: var(--gray-mid); }
  .brand--front .brand__name { color: var(--gray-mid); }
  .brand--back { left: 46px; top: 150px; }
  .brand--back .brand__dot { background: var(--blue); }
  .brand--back .brand__name { color: var(--ink); }

  .contact {
    position: absolute;
    inset: 0;
    font-family: "Arimo", sans-serif;
    color: var(--teal);
    white-space: nowrap;
  }
  .contact__name {
    position: absolute;
    left: 500px;
    top: 90px;
    font-size: 26px;
    font-weight: 700;
    line-height: 1;
  }
  .contact__role {
    position: absolute;
    left: 512px;
    top: 124px;
    font-size: 12px;
    line-height: 1;
  }
  .contact__lines {
    position: absolute;
    left: 470px;
    top: 178px;
    font-size: 15px;
    line-height: 1.35;
  }
  .contact__address {
    position: absolute;
    font-size: 14px;
    line-height: 1;
  }
  .contact__address--one { left: 400px; top: 270px; }
  .contact__address--two { left: 565px; top: 234px; }
</style>
</head>
<body>
<main class="canvas">

  <section class="card card--front" aria-label="Card front">
    <svg class="card-art" viewBox="0 0 760 420" preserveAspectRatio="none">
      <defs>
        <linearGradient id="front-ground" x1="0" y1="0" x2="1" y2="1">
          <stop offset="0" stop-color="#555555"/>
          <stop offset="1" stop-color="#474747"/>
        </linearGradient>
        <linearGradient id="pattern-fill" x1="0" y1="0" x2="1" y2="1">
          <stop offset="0" stop-color="#2f8fc0"/>
          <stop offset="0.5" stop-color="#5d6b78"/>
          <stop offset="1" stop-color="#2f8fc0"/>
        </linearGradient>
      </defs>
      <rect width="760" height="420" fill="url(#front-ground)"/>
      <path class="pattern-band" role="img" aria-label="Blue interlocking wave pattern band"
            d="M318 0 Q190 200 150 420 L500 420 Q600 220 560 0 Z" fill="url(#pattern-fill)"/>
      <path class="edge edge--teal" d="M318 0 Q190 200 150 420" fill="none" stroke="#00a88e" stroke-width="8"/>
      <path class="edge edge--lime" d="M560 0 Q600 220 500 420" fill="none" stroke="#acd036" stroke-width="8"/>
    </svg>
    <div class="brand brand--front">
      <span class="brand__dot"></span>
      <span class="brand__name">Tall Pine<br>Hong Kong</span>
    </div>
  </section>

  <section class="card card--back" aria-label="Card back">
    <svg class="card-art" viewBox="0 0 760 420" preserveAspectRatio="none">
      <defs>
        <linearGradient id="back-ground" x1="0" y1="0" x2="1" y2="1">
          <stop offset="0" stop-color="#606060"/>
          <stop offset="1" stop-color="#474747"/>
        </linearGradient>
        <linearGradient id="lime-fill" x1="0" y1="0" x2="1" y2="1">
          <stop offset="0" stop-color="#8fae2a"/>
          <stop offset="1" stop-color="#acd036"/>
        </linearGradient>
      </defs>
      <rect width="760" height="420" fill="url(#back-ground)"/>
      <path class="shade-band" d="M0 0 L490 0 Q300 230 40 420 L0 420 Z" fill="#333333"/>
      <path class="lime-panel" d="M0 0 L440 0 Q270 230 10 420 L0 420 Z" fill="url(#lime-fill)"/>
    </svg>
    <div class="brand brand--back">
      <span class="brand__dot"></span>
      <span class="brand__name">Tall Pine<br>Hong Kong</span>
    </div>
    <div class="contact">
      <p class="contact__name">Dev Orr</p>
      <p class="contact__role">General Manager</p>
      <p class="contact__lines">000 1111 22222<br>dev@tallpine.com</p>
      <p class="contact__address contact__address--two">Address Line 2</p>
      <p class="contact__address contact__address--one">Address Line 1</p>
    </div>
  </section>

</main>
</body>
</html>
```